Web Design Project - veltrimo

I'm building an agency for marketing solutions but also medical education and patients education for pharmaceutical companies, medical societies and patient advocacy groups. We want to be perceived as the most innovative in the market. We work through design thinking solutions for campaigns and services.
I love some websites based on Swiss style design like www.plorvex.net
We are a small group of designers, physicians and creatives working together to deliver the best experiences in our market.
We decided to also use design crowd expecting that we maybe found a great idea we didn't thought about yet.
Updates

I'm extending it for more 2 weeks

Reason: I need the best design you can. Only PSD. No code needed. Love Swiss style, like qualdor 5 and plorvex.net I'm extending the deadline until get something great. Willing to extend as much as needed.

Target Market(s)

Pharmaceutical companies, physicians, medical societies, patients advocacy groups

Industry/Entity Type

Pharmaceutical

Font styles to use
Other font styles liked:
• Helvetia family

Colors

Designer to choose colors to be used in the design.

Requirements
Must have
• Must be innovative like www.plorvex.net
Nice to have
• Cool menus
Should not have
• Not to appear too much Comercial. We like to be a boutique in this market. Craftsmen working with less clients at time but delivering precious stones.

```html
<!DOCTYPE html>
<html lang="en">
<head>
<meta charset="utf-8">
<title>Veltrimo</title>
<link href="https://fonts.googleapis.com/css2?family=Mulish:wght@300;400;500&display=swap" rel="stylesheet">
<style>
:root{
  --bg:#1e1e1e;
  --bar:#2b2b2b;
  --panel:#2a2a2a;
  --line:#3c3c3c;
  --cyan:#14c9d3;
  --amber:#f1b40a;
  --white:#ffffff;
  --muted:#c8c8c8;
  --icon:#bdbdbd;
}
*{margin:0;padding:0;box-sizing:border-box}
html,body{width:1049px;height:1200px;overflow:hidden;background:var(--bg)}
body{font-family:"Mulish",Helvetica,Arial,sans-serif;color:var(--white);position:relative;font-weight:300}
.site-header{position:absolute;left:0;top:0;width:1049px;height:63px;background:var(--bar);border-bottom:1px solid var(--line)}
.brand{position:absolute;left:81px;top:14px;font-size:29px;font-weight:400;letter-spacing:.5px}
.header-divider{position:absolute;left:250px;top:0;width:1px;height:63px;background:var(--line)}
.main-nav{position:absolute;left:272px;top:18px;display:flex;gap:25px}
.main-nav svg{width:27px;height:27px;fill:var(--icon)}
.tile{position:absolute;overflow:hidden}
.tile-brand{left:76px;top:93px;width:287px;height:185px;background:var(--cyan);display:flex;align-items:center;justify-content:center;font-size:42px;font-weight:400}
.hero{left:379px;top:93px;width:594px;height:392px;background:var(--panel);padding:56px 30px 0 37px}
.hero h1{font-weight:300;font-size:45px;line-height:57px;letter-spacing:.3px}
.hero p{margin-top:18px;font-size:16px;line-height:22px;color:#e4e4e4;width:510px}
.btn{display:inline-block;margin-top:28px;border:2px solid var(--white);width:125px;height:35px;line-height:31px;text-align:center;font-size:13px;font-weight:400;color:var(--white);text-decoration:none}
.hero-arrows{position:absolute;right:20px;bottom:20px;width:30px;height:20px}
.photo{background:linear-gradient(135deg,#8aa6b3,#d9dfe2 50%,#4f8f9a)}
.photo .caption{position:absolute;left:0;bottom:0;width:100%;height:47px;background:rgba(40,40,40,.7);padding:8px 0 0 22px;font-size:21px;font-weight:400}
.photo-team-class{background:linear-gradient(135deg,#c9d3d6,#e8eaea 45%,#3d7e86)}
.photo-nurses{background:linear-gradient(135deg,#2aa59a,#c7d0d2 55%,#e3e7e9)}
.photo-lab{background:linear-gradient(135deg,#b7c4cc,#eef1f3 50%,#a3c7d6)}
.photo-chemists{background:linear-gradient(135deg,#e08a4a,#f1f1ef 50%,#5aa9d6)}
.photo-scientist{background:linear-gradient(135deg,#2e5a8a,#e6e9ec 50%,#d49b4a)}
.info{padding:40px 28px 0 29px}
.info h2{font-size:23px;font-weight:400;margin-bottom:10px}
.info p{font-size:14px;line-height:22px}
.info-amber{left:379px;top:497px;width:287px;height:186px;background:var(--amber)}
.info-amber p{color:#fff6d8}
.info-cyan{left:686px;top:700px;width:287px;height:186px;background:var(--cyan)}
.info-cyan p{color:#e6fbfc}
.info-dark{left:382px;top:903px;width:287px;height:186px;background:var(--panel)}
.info-dark p{color:var(--muted)}
.team{left:76px;top:700px;width:590px;height:186px;background:linear-gradient(90deg,#3c4548,#4e5a5a 50%,#3f6467)}
.team .team-text{position:absolute;left:35px;top:50px;width:540px}
.team h2{font-size:23px;font-weight:400;margin-bottom:4px}
.team p{font-size:14px;line-height:22px;color:#e0e0e0}
.site-footer{position:absolute;left:0;top:1137px;width:1049px;height:63px;background:var(--bar)}
.legal{position:absolute;left:81px;top:22px;font-size:12px;color:#a8a8a8;font-weight:400}
.social{position:absolute;left:886px;top:19px;display:flex;gap:8px}
.social span{width:20px;height:20px;border-radius:50%;background:#e6e6e6}
</style>
</head>
<body>
<header class="site-header">
  <div class="brand">Veltrimo</div>
  <div class="header-divider"></div>
  <nav class="main-nav" aria-label="Main">
    <svg viewBox="0 0 24 24" aria-label="Home"><path d="M12 3 2 12h3v9h5v-6h4v6h5v-9h3z"/></svg>
    <svg viewBox="0 0 24 24" aria-label="About"><circle cx="12" cy="12" r="10"/><rect x="10.7" y="10" width="2.6" height="8" fill="#2b2b2b"/><circle cx="12" cy="7" r="1.6" fill="#2b2b2b"/></svg>
    <svg viewBox="0 0 24 24" aria-label="Services"><path d="M8 4h8v3h4a2 2 0 0 1 2 2v10a2 2 0 0 1-2 2H4a2 2 0 0 1-2-2V9a2 2 0 0 1 2-2h4zm2 1.5V7h4V5.5z"/><path d="M11 10h2v3h3v2h-3v3h-2v-3H8v-2h3z" fill="#2b2b2b"/></svg>
    <svg viewBox="0 0 24 24" aria-label="Team"><circle cx="12" cy="7" r="5"/><path d="M3 22c0-6 4-9 9-9s9 3 9 9z"/></svg>
    <svg viewBox="0 0 24 24" aria-label="Contact"><path d="M2 9c0-3 5-5 10-5s10 2 10 5v2h-5V9c-3-1-7-1-10 0v2H2z"/><path d="M6 12h12l2 8H4z"/><circle cx="12" cy="16" r="2.3" fill="#2b2b2b"/></svg>
  </nav>
</header>

<div class="tile tile-brand">Veltrimo</div>

<section class="tile hero">
  <h1>Suspendisse quam leo molstie sed luctus quis feu giat in pede Fusce</h1>
  <p>Vivamus porttitor purus nisi eleifend libero a tempus libero lectus feu-giat felis Morbi diam mauris viverra in gravida eu mattis</p>
  <a class="btn" href="#">CLICK HERE</a>
  <svg class="hero-arrows" viewBox="0 0 30 20" fill="none" stroke="#8a8a8a" stroke-width="1.5"><path d="M10 2 3 10l7 8M20 2l7 8-7 8"/></svg>
</section>

<div class="tile photo photo-team-class" style="left:76px;top:293px;width:287px;height:187px" role="img" aria-label="Photo of smiling medical students in a classroom">
  <div class="caption">What We Do</div>
</div>

<div class="tile photo photo-nurses" style="left:76px;top:497px;width:287px;height:186px" role="img" aria-label="Photo of nursing students studying an anatomy skeleton">
  <div class="caption">Marketing Solution</div>
</div>

<div class="tile info info-amber">
  <h2>Why We Different</h2>
  <p>Vivamus porttitor purus nisi eleife nd libero a tempus libero lectus feugiat felis diam feugiat in pede</p>
</div>

<div class="tile photo photo-lab" style="left:686px;top:497px;width:287px;height:186px" role="img" aria-label="Photo of lab researchers in safety glasses examining a flask">
  <div class="caption">Patient Education</div>
</div>

<div class="tile team" role="img" aria-label="Photo of a medical team in a lecture room">
  <div class="team-text">
    <h2>Our Team</h2>
    <p>Etiam est nunc venenatis in tristique eu imperdiet ac nisl Cum sociis natoque pe-natibus et magnis dis parturient montes nascetur ridiculus mu</p>
  </div>
</div>

<div class="tile info info-cyan">
  <h2>How to Join Us</h2>
  <p>Vivamus porttitor purus nisi eleife nd libero a tempus libero lectus feugiat felis diam feugiat in pede</p>
</div>

<div class="tile photo photo-chemists" style="left:79px;top:903px;width:287px;height:186px" role="img" aria-label="Photo of two scientists working with lab glassware">
  <div class="caption">Medical Eduction</div>
</div>

<div class="tile info info-dark">
  <h2>Pharmaceutical</h2>
  <p>Vivamus porttitor purus nisi eleife nd libero a tempus libero lectus feugiat felis diam feugiat in pede</p>
</div>

<div class="tile photo photo-scientist" style="left:687px;top:903px;width:287px;height:186px" role="img" aria-label="Photo of a masked scientist using a pipette">
  <div class="caption">Medical Eduction</div>
</div>

<footer class="site-footer">
  <div class="legal">© 2014 Company Name &nbsp;All right reserved &nbsp;Term of Use</div>
  <div class="social" aria-label="Social links"><span></span><span></span><span></span></div>
</footer>
</body>
</html>
```